Auto Parts Brochure

We need a marketing catalogue created. I have attached 4 examples of our inventory to use when creating an example of the catalogue, along with our logos etc. The example should use our corporate colors of Red, Yellow and black.

For the final catalogue, we have over 100 items of inventory to list.

Font styles to use
Sans Serif

Colors
f78f20
f04a50

```html
<!DOCTYPE html>
<html lang="en">
<head>
<meta charset="utf-8">
<title>Dialworks Catalogue – Page 1</title>
<link href="https://fonts.googleapis.com/css2?family=Montserrat:wght@800;900&family=Raleway:wght@400;500;600&display=swap" rel="stylesheet">
<style>
  :root {
    --ink: #2b2b2b;
    --ink-deep: #1f1f1f;
    --red: #ea4450;
    --yellow: #f3ca46;
    --paper: #f7f7f7;
    --stage: #ececec;
    --grey: #b9b9b9;
    --text: #333333;
    --photo-grey: #cfcfcf;
  }
  * { box-sizing: border-box; margin: 0; padding: 0; }
  html, body { width: 1200px; height: 900px; overflow: hidden; }
  body {
    background: var(--stage);
    display: flex; align-items: center; justify-content: center;
    font-family: "Raleway", Arial, sans-serif;
    color: var(--text);
  }
  .page {
    position: relative;
    width: 600px; height: 860px;
    background: var(--paper);
    overflow: hidden;
  }
  .page-art { position: absolute; inset: 0; width: 100%; height: 100%; }

  .hero { position: absolute; left: 44px; top: 70px; width: 360px; }
  .hero-kicker {
    font-family: "Montserrat", Arial, sans-serif; font-weight: 800;
    color: var(--yellow); font-size: 15px; letter-spacing: .3px;
  }
  .hero-title {
    font-family: "Montserrat", Arial, sans-serif; font-weight: 900;
    color: var(--red); font-size: 44px; line-height: 1; margin-top: 4px;
  }
  .hero-copy {
    color: #ffffff; font-size: 12.5px; font-weight: 600; line-height: 1.55;
    margin-top: 12px; width: 290px;
  }

  .product-photo { position: absolute; border-radius: 6px; }
  .photo-cutout { background: radial-gradient(ellipse at 50% 50%, #4a4a4a 0%, #1d1d1d 70%); border-radius: 46% 46% 40% 40% / 60% 60% 40% 40%; }
  .photo-framed { background: linear-gradient(135deg, #d8d8d8, #bcbcbc); border-radius: 0; padding: 14px; }
  .photo-framed::after {
    content: ""; position: absolute; inset: 16px 12px;
    background: radial-gradient(ellipse at 50% 55%, #3a3a3a 0%, #191919 75%);
    border-radius: 40% 40% 30% 30% / 55% 55% 35% 35%;
  }

  .item { position: absolute; font-size: 10.5px; line-height: 1.45; }
  .item-name { font-size: 12px; font-weight: 500; letter-spacing: .3px; color: var(--ink); }
  .spec { display: grid; grid-template-columns: 42px 1fr; }

  .divider { position: absolute; height: 1px; background: #555; }

  .brand {
    position: absolute; left: 30px; bottom: 56px;
    display: flex; align-items: center; gap: 6px;
    font-family: "Raleway", Arial, sans-serif; font-weight: 600;
    font-size: 15px; color: var(--ink);
  }
  .brand-dot { width: 12px; height: 12px; border-radius: 50%; background: var(--red); }

  .progress {
    position: absolute; left: 150px; bottom: 22px;
    display: flex; gap: 4px; align-items: center;
  }
  .progress span { width: 28px; height: 8px; }
  .progress .seg-grey { background: var(--grey); }
  .progress .seg-yellow { background: var(--yellow); }
  .progress .seg-red { background: var(--red); }
  .page-number {
    width: 20px !important; height: 16px !important; background: var(--ink);
    color: #fff; font-size: 9px; font-weight: 600;
    display: flex; align-items: center; justify-content: center;
  }
</style>
</head>
<body>
  <main class="page">
    <svg class="page-art" viewBox="0 0 600 860" preserveAspectRatio="none" aria-hidden="true">
      <polygon points="0,0 600,0 600,190 480,300 0,300" fill="var(--ink-deep)"/>
      <polygon points="470,150 600,85 600,470 560,470" fill="var(--red)"/>
      <polygon points="540,250 560,470 330,360" fill="var(--yellow)"/>
    </svg>

    <header class="hero">
      <p class="hero-kicker">Lorem Ipsum Dolor Sit Amet</p>
      <h1 class="hero-title">Consectetuer Adipiscing</h1>
      <p class="hero-copy">Lorem ipsum dolor sit amet, consectetuer adipiscing elit, sed diam nonummy nibh euismod tincidunt ut laoreet dolore magna aliquam erat volutpat. Ut wisi enim ad minim</p>
    </header>

    <div class="product-photo photo-cutout" role="img" aria-label="Photo of a black speedometer dial face" style="left:60px; top:330px; width:230px; height:110px;"></div>
    <div class="item" style="left:44px; top:448px; width:270px;">
      <p class="item-name">LOREM IPSUM</p>
      <p>Samet, consectetuer adipiscing elit, sed diam erat volutpat.</p>
      <div class="spec"><span>Ut wisi</span><span>: enim ad</span><span>Minim</span><span>: veniam</span><span>Quis</span><span>: Nostrud exerci tation</span></div>
    </div>

    <div class="product-photo photo-framed" role="img" aria-label="Photo of an instrument cluster with twin gauges" style="left:330px; top:420px; width:250px; height:130px;"></div>
    <div class="item" style="left:330px; top:560px; width:250px;">
      <p class="item-name">LOREM IPSUM</p>
      <p>A adipiscing elit, sed diam nonummy nibh euismod dolore magna aliquam erat volutpat.</p>
      <div class="spec"><span>Ut wisi</span><span>: enim ad</span><span>Minim</span><span>: veniam</span><span>Quis</span><span>: Nostrud exerci tation</span></div>
    </div>

    <div class="divider" style="left:44px; top:540px; width:270px;"></div>

    <div class="item" style="left:44px; top:552px; width:270px;">
      <p class="item-name">LOREM IPSUM</p>
      <p>St amet, nibh euismod tincidunt ut laoreet dolore magna aliquam erat volutpat.</p>
      <div class="spec"><span>Ut wisi</span><span>: enim ad</span><span>Minim</span><span>: veniam</span><span>Quis</span><span>: Nostrud exerci tation</span></div>
    </div>

    <div class="divider" style="left:330px; top:655px; width:250px;"></div>

    <div class="product-photo photo-cutout" role="img" aria-label="Photo of a full black gauge cluster dial set" style="left:340px; top:670px; width:230px; height:100px;"></div>

    <div class="product-photo photo-framed" role="img" aria-label="Photo of a single round black gauge face" style="left:44px; top:660px; width:110px; height:95px;"></div>
    <div class="item" style="left:170px; top:662px; width:160px;">
      <p class="item-name">LOREM IPSUM</p>
      <p>Consectetuer adipiscing elit, sed diam nonummy nibh euismod aliquam erat.</p>
      <div class="spec"><span>Ut wisi</span><span>: enim ad</span><span>Minim</span><span>: veniam</span><span>Quis</span><span>: Nostrud exerci</span></div>
    </div>

    <div class="brand"><span class="brand-dot"></span>Dialworks</div>

    <nav class="progress" aria-label="Catalogue sections">
      <span class="seg-grey"></span><span class="seg-grey"></span><span class="seg-grey"></span><span class="seg-grey"></span>
      <span class="seg-yellow"></span><span class="seg-yellow"></span><span class="seg-yellow"></span><span class="seg-yellow"></span>
      <span class="seg-red"></span><span class="seg-red"></span><span class="seg-red"></span><span class="seg-red"></span>
      <span class="page-number">1</span>
    </nav>
  </main>
</body>
</html>
```